Velmora Land Surveying Website Design

We are working with Velmora. They are a national land surveying company and in need of a new website design.

Some sites to use for inspiration:

https://brannockeng.com
https://www.qlvinc.com
https://dervanto.com
https://gkw.us
https://corvenbuilt.com
https://www.pellacombwendrix.com

Thank you for taking the time to consider designing a website for us. We are web developers based in Stockton and Los Angeles, CA, USA. Most of our projects go through the same process. Understanding this process may help you win a project with us. We custom-code all of our websites in-house. We don’t have any requirements as to what tools you use for your design, but we prefer Figma files. For any design that we label as four-stars, we send it to the client for review. The client picks the final design they want us to use. Once we complete this process, we will continue to show additional clients all the four-star sites and purchase them later. Your designs will have multiple chances to sell. For better chances of success, we ask that you follow these guidelines.

IMAGES:
If you use any images or icons in the design, we ask that you have a link to the asset so we can purchase the image/icon. Most of the designs we submit do not have the customer’s images on them unless they have some great images. Be creative; show us the feeling you are trying to portray with your image choices. Use any royalty-free site you choose. We subscribe to Quillar and mainly use their images, but we can purchase images outside of Quillar.

PLEASE NOTE: we will not submit designs to clients with watermarks on the images.

FONTS:
We ask that you identify the fonts used in the design. This can be done in a message if you want. We typically use Google Fonts and Quillar Fonts.

CONTENT:
We're always open to different content and ideas. We often submit designs with stock images so the client can see our vision. We typically take pictures after the website launch to use their images with our vision. Lorem Ipsum is fine for paragraphs, but we ask that you write the headers in correct English. We want to be able to show the vision and identify the sections of the website.

INSPIRATION:
We typically add a couple of links in the brief of websites we like to help you get started in your design.

REVISIONS:
We do not often ask for revisions of the designs unless we see something in the design that may not appeal to the client. If there are slight changes that we want to make, we do that in the development process.

FEEDBACK:
We rarely give feedback on designs during the design process. We are working on many website projects and do not have the time to provide feedback. We usually respond if your request is well thought out and asks specific questions, but a note asking “feedback, please” usually goes unanswered.

```html
<!DOCTYPE html>
<html lang="en">
<head>
<meta charset="utf-8">
<title>Velmora Land Surveying</title>
<link href="https://fonts.googleapis.com/css2?family=Teko:wght@400;500;600&family=Poppins:wght@400;500;600&display=swap" rel="stylesheet">
<style>
:root{
  --red:#e3211f;
  --red-dark:#c81b19;
  --ink:#111;
  --text:#444;
  --muted:#666;
  --dark:#262626;
  --white:#fff;
}
*{margin:0;padding:0;box-sizing:border-box}
html,body{width:1200px;height:4854px;overflow:hidden}
body{position:relative;background:var(--white);font-family:'Poppins',sans-serif;color:var(--text)}
.abs{position:absolute}
.head{font-family:'Teko',sans-serif;font-weight:600;text-transform:uppercase;line-height:1;color:var(--red)}
.sub{font-family:'Teko',sans-serif;font-weight:400;text-transform:uppercase;color:#555;font-size:26px;display:flex;align-items:center;gap:12px;line-height:1}
.sub .rule{display:inline-block;width:56px;height:2px;background:currentColor}
.btn{position:absolute;display:flex;align-items:center;justify-content:center;gap:14px;background:var(--red);color:#fff;border-radius:40px;font-weight:600;text-transform:uppercase;font-size:19px}
.btn svg{width:22px;height:22px}
.photo{position:absolute}

/* header */
.logo{left:68px;top:34px;display:flex;align-items:center;gap:14px}
.logo .mark{width:58px;height:58px;border-radius:50%;background:var(--red)}
.logo .name{font-family:'Teko',sans-serif;font-weight:600;font-size:58px;color:var(--red);line-height:1;text-transform:uppercase}
.search{left:738px;top:28px;width:250px;height:40px;border:1.5px solid #999;border-radius:20px;font-size:14px;color:#999;padding:9px 18px}
.search svg{position:absolute;right:14px;top:10px}
.top-contact{left:996px;top:28px;width:141px;height:40px;font-size:15px;font-weight:500;text-transform:none}
.nav{left:530px;top:92px;width:610px;display:flex;justify-content:space-between;font-size:13px;color:#333;text-transform:uppercase}
.nav .active{color:var(--red);border-bottom:2px solid var(--red);padding-bottom:6px}

/* hero */
.hero{left:0;top:143px;width:1200px;height:684px;background:linear-gradient(120deg,#3d3326 0%,#5a5a3a 40%,#4f6a3a 70%,#6c7a52 100%)}
.hero-shade{left:0;top:143px;width:1200px;height:684px;background:linear-gradient(90deg,rgba(0,0,0,.55),rgba(0,0,0,0))}
.hero-kicker{left:68px;top:262px;font-size:36px;font-weight:500;display:flex;align-items:center;gap:14px}
.hero-kicker .rule{width:84px;height:2px;background:#fff;display:inline-block}
.hero-title{left:66px;top:300px;font-size:88px;line-height:.86;color:#fff}
.hero-title span{color:var(--red)}
.hero-text{left:68px;top:486px;width:660px;color:#fff;font-size:21px;line-height:1.75}
.hero-btn{left:68px;top:630px;width:220px;height:64px}

/* about */
.about-frame{left:79px;top:932px;width:794px;height:444px;border:2px solid var(--red)}
.about-title{left:542px;top:1375px;font-size:68px}
.about-sub{left:542px;top:1437px}
.lead{font-size:16px;font-weight:600;color:var(--ink);line-height:1.65;text-align:justify}
.body-text{font-size:13.5px;line-height:2;color:#555;text-align:justify}
.about-lead{left:540px;top:1498px;width:586px}
.about-text{left:540px;top:1572px;width:586px}
.about-btn{left:542px;top:1695px;width:210px;height:63px}

/* why */
.why{left:0;top:1862px;width:1200px;height:523px;background:linear-gradient(180deg,#3a3f32,#2e2e2b 60%,#3a3b33)}
.why-shade{left:0;top:1862px;width:1200px;height:523px;background:rgba(20,20,20,.55)}
.why-title{left:0;top:1935px;width:1200px;text-align:center;font-size:68px}
.why-sub{left:0;top:1998px;width:1200px;justify-content:center;color:#fff}
.why-text{left:0;top:2061px;width:1200px;text-align:center;color:#fff;font-size:14.5px}
.stat{position:absolute;top:2130px;width:120px;height:123px}
.stat .back{position:absolute;left:10px;top:0;width:110px;height:113px;background:var(--red)}
.stat .front{position:absolute;left:0;top:10px;width:110px;height:113px;border:2px solid #fff;display:flex;align-items:center;justify-content:center;font-family:'Teko',sans-serif;font-size:50px;font-weight:500;color:#fff}
.stat-label{position:absolute;top:2276px;width:240px;text-align:center;color:#fff;font-size:17px;text-transform:uppercase}

/* services */
.svc-title{left:0;top:2500px;width:1200px;text-align:center;font-size:68px}
.svc-sub{left:0;top:2565px;width:1200px;justify-content:center}
.svc-text{left:140px;top:2638px;width:920px;text-align:center;font-size:13.5px;line-height:2;color:#555}
.card-img{position:absolute;top:2745px;width:332px;height:255px}
.card-body{position:absolute;top:2933px;width:292px;height:230px;background:#fff;padding:36px 12px 0 38px}
.card-body h3{font-family:'Teko',sans-serif;font-weight:600;font-size:26px;color:var(--red);text-transform:uppercase;line-height:1}
.card-body p{margin-top:6px;font-size:13.5px;line-height:1.85;color:#555;text-align:justify}
.card-body .small-btn{display:inline-block;margin-top:12px;background:var(--red);color:#fff;font-size:11px;font-weight:600;padding:6px 16px;border-radius:14px;text-transform:uppercase}
.arrow{position:absolute;top:3220px;width:46px;height:46px;border-radius:50%;display:flex;align-items:center;justify-content:center}

/* join */
.join-frame{left:68px;top:3365px;width:1009px;height:445px;border:2px solid var(--red)}
.join-box{left:237px;top:3750px;width:726px;height:210px;background:#fff}
.join-title{left:0;top:3800px;width:1200px;text-align:center;font-size:72px}
.join-sub{left:0;top:3872px;width:1200px;justify-content:center}
.join-lead{left:305px;top:3938px;width:590px;text-align:center}
.join-text{left:300px;top:4010px;width:600px;text-align:center}
.join-btn{left:495px;top:4127px;width:210px;height:64px}

/* newsletter + footer */
.footer{left:0;top:4395px;width:1200px;height:459px;background:var(--dark)}
.news{left:70px;top:4335px;width:1063px;height:120px;background:var(--red)}
.news-title{left:205px;top:4378px;font-size:44px;color:#fff}
.news-input{left:616px;top:4375px;width:382px;height:40px;background:#fff;border-radius:20px;font-size:10px;color:#777;padding:13px 24px}
.news-btn{left:882px;top:4375px;width:116px;height:40px;background:var(--dark);color:#fff;border-radius:20px;font-size:14px;font-weight:500;display:flex;align-items:center;justify-content:center}
.f-logo{left:120px;top:4608px;display:flex;align-items:center;gap:20px}
.f-logo .mark{width:92px;height:92px;border-radius:50%;background:var(--red)}
.f-logo .name{font-family:'Teko',sans-serif;font-weight:600;font-size:84px;color:var(--red);line-height:1;text-transform:uppercase}
.f-head{font-family:'Teko',sans-serif;font-weight:500;font-size:26px;color:#fff;text-transform:uppercase;line-height:1}
.f-head::after{content:"";display:block;width:52px;height:2px;background:var(--red);margin-top:6px}
.links{left:608px;top:4600px;list-style:none;color:#fff;font-size:13.5px;line-height:26px}
.links li::before{content:"";display:inline-block;width:8px;height:8px;border-radius:50%;background:var(--red);margin-right:16px;vertical-align:1px}
.contact{position:absolute;left:855px;display:flex;gap:14px;color:#fff;font-size:13px;line-height:1.3}
.contact .ic{width:34px;height:34px;border-radius:50%;background:var(--red);display:flex;align-items:center;justify-content:center;flex:none}
.copy{left:70px;top:4812px;color:#fff;font-size:11px}
.social{position:absolute;top:4810px;width:24px;height:24px;border-radius:50%;background:var(--red)}
</style>
</head>
<body>

<!-- header -->
<div class="abs logo"><span class="mark"></span><span class="name">Velmora</span></div>
<div class="abs search">Search...
  <svg width="18" height="18" viewBox="0 0 20 20" fill="none" stroke="#999" stroke-width="2"><circle cx="8" cy="8" r="6"/><path d="M13 13l5 5"/></svg>
</div>
<div class="btn top-contact">Contact Us</div>
<nav class="abs nav">
  <span class="active">Home</span><span>About Us</span><span>Our Services ▾</span><span>Projects</span><span>Careers</span>
</nav>

<!-- hero -->
<div class="abs hero" role="img" aria-label="Aerial photo of farmland with a dotted survey boundary and location pin"></div>
<div class="abs hero-shade"></div>
<div class="abs head hero-kicker">Velmora Land Surveying <span class="rule"></span></div>
<h1 class="abs head hero-title"><span style="color:#fff">Professional Land</span><br><span>Surveying &amp; Mapping</span></h1>
<p class="abs hero-text">Lorem ipsum dolor sit amet, consectetur adipi scing elit. Vi vamus finibus enim nec odio ultricies dictum. Donec vel nisl posuere, finibus ex vel.</p>
<div class="btn hero-btn">Contact Us
  <svg viewBox="0 0 24 24" fill="none" stroke="#fff" stroke-width="2"><circle cx="12" cy="12" r="9"/><path d="M8 12h8M13 9l3 3-3 3"/></svg>
</div>

<!-- about -->
<div class="abs about-frame"></div>
<svg class="photo" style="left:103px;top:964px" width="890" height="499" role="img" aria-label="Photo of engineers in hard hats reviewing plans at a building site">
  <defs><linearGradient id="ga" x1="0" y1="0" x2="1" y2="1"><stop offset="0" stop-color="#c9c2b4"/><stop offset=".5" stop-color="#9a6e54"/><stop offset="1" stop-color="#6c86a6"/></linearGradient></defs>
  <path d="M0 0H890V353H360V499H0Z" fill="url(#ga)"/>
</svg>
<h2 class="abs head about-title">About Us</h2>
<div class="abs sub about-sub">Who We Are <span class="rule"></span></div>
<p class="abs lead about-lead">Lorem ipsum dolor sit amet, consectetur adipiscing elit. Aenean semper nunc urna, sit amet lobortis erat scelerisque sit amet.</p>
<p class="abs body-text about-text">Lorem ipsum dolor sit amet, consectetur adipiscing elit, sed do ei usmod tempor inc ididunt ut labore et dolore magna aliqua. Ut enim ad minim veniam, quis nostrud ex ercitation ullamco laboris nisi ut aliquip ex ea commodo consequat.</p>
<div class="btn about-btn">Read More
  <svg viewBox="0 0 24 24" fill="none" stroke="#fff" stroke-width="2"><circle cx="12" cy="12" r="9"/><path d="M8 12h8M13 9l3 3-3 3"/></svg>
</div>

<!-- why choose us -->
<div class="abs why" role="img" aria-label="Landscape photo of green hills and fields"></div>
<div class="abs why-shade"></div>
<h2 class="abs head why-title">Why Choose Us?</h2>
<div class="abs sub why-sub"><span class="rule"></span> Velmora Land Surveying <span class="rule"></span></div>
<p class="abs why-text">Lorem ipsum dolor sit amet, consectetur adipiscing elit. Etiam in vestibulum urna. Quisque in lectus non sem consequat</p>
<div class="stat" style="left:185px"><div class="back"></div><div class="front">150+</div></div>
<div class="stat" style="left:425px"><div class="back"></div><div class="front">240+</div></div>
<div class="stat" style="left:673px"><div class="back"></div><div class="front">1200+</div></div>
<div class="stat" style="left:911px"><div class="back"></div><div class="front">50+</div></div>
<div class="stat-label" style="left:131px">Leed Professionals</div>
<div class="stat-label" style="left:370px">Satisfied Clients</div>
<div class="stat-label" style="left:617px">Projects Done</div>
<div class="stat-label" style="left:857px">Awards Won</div>

<!-- services -->
<h2 class="abs head svc-title">Our Services</h2>
<div class="abs sub svc-sub"><span class="rule"></span> What We Do <span class="rule"></span></div>
<p class="abs svc-text">Lorem ipsum dolor sit amet, consectetur adipiscing elit, sed do eiusmod tempor incididunt ut labore et dolore magna aliqua. Quis ipsum suspendisse ultrices gravida. Risus commodo viverra maecenas accumsan lacus vel facilisis.</p>

<div class="card-img" style="left:70px;background:linear-gradient(135deg,#cfd3d6,#c46a2e 55%,#8a8f94)" role="img" aria-label="Photo of workers in safety vests reviewing plans"></div>
<div class="card-body" style="left:110px"><h3>Emergency Planning</h3><p>Lorem ipsum dolor sit amet, consec tetur adipiscing elit, sed do eiusmod tempor incididunt ut labore et dolore</p><span class="small-btn">Read More</span></div>

<div class="card-img" style="left:438px;background:linear-gradient(135deg,#9aa3a8,#e07a2a 45%,#5b5f62)" role="img" aria-label="Photo of a surveyor using a total station"></div>
<div class="card-body" style="left:478px"><h3>Surveying &amp; Mapping</h3><p>Lorem ipsum dolor sit amet, consec tetur adipiscing elit, sed do eiusmod tempor incididunt ut labore et dolore</p><span class="small-btn">Read More</span></div>

<div class="card-img" style="left:801px;background:linear-gradient(135deg,#e4e7ea,#a9adb2 50%,#3c3f44)" role="img" aria-label="Photo of a construction team inspecting a building interior"></div>
<div class="card-body" style="left:841px"><h3>Construction Management</h3><p>Lorem ipsum dolor sit amet, consec tetur adipiscing elit, sed do eiusmod tempor incididunt ut labore et dolore</p><span class="small-btn">Read More</span></div>

<div class="arrow" style="left:552px;background:#e2e2e2"><svg width="16" height="16" viewBox="0 0 16 16" fill="none" stroke="#777" stroke-width="2"><path d="M10 3L5 8l5 5"/></svg></div>
<div class="arrow" style="left:611px;background:#666"><svg width="16" height="16" viewBox="0 0 16 16" fill="none" stroke="#fff" stroke-width="2"><path d="M6 3l5 5-5 5"/></svg></div>

<!-- join us -->
<div class="abs join-frame"></div>
<div class="photo" style="left:93px;top:3397px;width:1041px;height:503px;background:linear-gradient(90deg,#9fb0c2,#6d88a6 40%,#b58a68 75%,#e0662a)" role="img" aria-label="Photo of a construction worker in a white hard hat at a building site"></div>
<div class="abs join-box"></div>
<h2 class="abs head join-title">Join Us</h2>
<div class="abs sub join-sub"><span class="rule"></span> Talk To Us <span class="rule"></span></div>
<p class="abs lead join-lead">Lorem ipsum dolor sit amet, consectetur adipiscing elit. Aenean semper nunc urna, sit amet lobortis erat scelerisque sit amet.</p>
<p class="abs body-text join-text" style="text-align:center">Lorem ipsum dolor sit amet, consectetur adipiscing elit, sed do ei usmod tempor inc ididunt ut labore et dolore magna aliqua. Ut enim ad minim veniam, quis nostrud ex ercitation ullamco laboris nisi ut aliquip ex ea commodo consequat.</p>
<div class="btn join-btn">Careers
  <svg viewBox="0 0 24 24" fill="none" stroke="#fff" stroke-width="2"><circle cx="12" cy="12" r="9"/><path d="M8 12h8M13 9l3 3-3 3"/></svg>
</div>

<!-- footer -->
<div class="abs footer"></div>
<div class="abs news"></div>
<h2 class="abs head news-title">Our Newsletter Sign Up</h2>
<div class="abs news-input">Enter Email Address</div>
<div class="abs news-btn">SIGNUP</div>

<div class="abs f-logo"><span class="mark"></span><span class="name">Velmora</span></div>

<div class="abs f-head" style="left:607px;top:4540px">Quick Links</div>
<ul class="abs links">
  <li>About Us</li><li>Services</li><li>Projects</li><li>Careers</li><li>Contact Us</li>
</ul>

<div class="abs f-head" style="left:855px;top:4540px">Contact Us</div>
<div class="contact" style="top:4610px"><span class="ic"><svg width="16" height="16" viewBox="0 0 24 24" fill="#fff"><path d="M6.6 10.8a15 15 0 006.6 6.6l2.2-2.2a1 1 0 011-.25 11.4 11.4 0 003.6.6 1 1 0 011 1V20a1 1 0 01-1 1A17 17 0 013 4a1 1 0 011-1h3.5a1 1 0 011 1c0 1.25.2 2.45.6 3.6a1 1 0 01-.25 1z"/></svg></span><div>CALL US<br>012 345 6789</div></div>
<div class="contact" style="top:4668px"><span class="ic"><svg width="16" height="16" viewBox="0 0 24 24" fill="#fff"><path d="M3 5h18v14H3z"/><path d="M3 5l9 7 9-7" stroke="#e3211f" stroke-width="2" fill="none"/></svg></span><div>EMAIL US<br>info@websitename.com</div></div>
<div class="contact" style="top:4726px"><span class="ic"><svg width="16" height="16" viewBox="0 0 24 24" fill="#fff"><path d="M12 2a7 7 0 00-7 7c0 5 7 13 7 13s7-8 7-13a7 7 0 00-7-7zm0 9.5a2.5 2.5 0 110-5 2.5 2.5 0 010 5z"/></svg></span><div>Address line Dummy Here<br>Address line Dummy</div></div>

<div class="abs copy">Copyright © 2025 All Rights Reserved By Company Name</div>
<span class="social" style="left:1016px"></span>
<span class="social" style="left:1047px"></span>
<span class="social" style="left:1078px"></span>
<span class="social" style="left:1109px"></span>

</body>
</html>
```